■デザインへの要望
1)フライヤーのイメージとしては明るく女性的なイメージを希望します。
2)人物写真は使わないでください。
3)コーポレートロゴを右上に配置してください。
ロゴの改変(色の変更や比率の変更)はご遠慮ください。
4)会のロゴを配置してください。
位置はお任せしますが、サイズの変更はご遠慮ください。
※前回のフライヤーを素材と一緒にお付けしますのでご参考になさってください。

■素材
1)フライヤーを作成する際に必要なロゴ等の画像等は

```html
<!DOCTYPE html>
<html lang="ja">
<head>
<meta charset="utf-8">
<title>ランチョンセミナー15 これからの摂食嚥下障害看護に何が求められているか</title>
<link rel="stylesheet" href="https://fonts.googleapis.com/css2?family=Noto+Sans+JP:wght@400;500;700;900&family=Noto+Serif+JP:wght@700;900&display=swap">
<style>
:root{
  --green:#3f9a3a;
  --green-dark:#2f7d2b;
  --ink:#1d1d1d;
  --white:#ffffff;
}
*{margin:0;padding:0;box-sizing:border-box}
html,body{width:875px;height:1200px;overflow:hidden;background:var(--white)}
body{font-family:"Noto Sans JP",sans-serif;color:var(--ink);position:relative}
.flyer{position:relative;width:875px;height:1200px;overflow:hidden}

.header{position:absolute;top:0;left:0;width:100%;height:198px;background:var(--white);text-align:center}
.society-mark{position:absolute;left:120px;top:26px;display:flex;align-items:center;gap:8px}
.society-mark .square{width:14px;height:14px;background:var(--green)}
.society-mark .name{font-size:15px;font-weight:700;color:var(--green)}
.sponsor-mark{position:absolute;right:34px;top:42px;display:flex;align-items:center;gap:10px}
.sponsor-mark .dot{width:28px;height:28px;border-radius:50%;background:var(--green)}
.sponsor-mark .name{font-size:30px;font-weight:900;color:var(--green);letter-spacing:1px}
.congress{position:absolute;top:112px;width:100%;font-size:25px;font-weight:700;color:var(--green-dark)}
.seminar-no{position:absolute;top:150px;width:100%;font-size:22px;font-weight:700;color:var(--green-dark)}

.floral-field{position:absolute;top:198px;left:0;width:100%;height:1002px;
  background:radial-gradient(ellipse 62% 42% at 50% 45%,#fffbe4 0%,#fcf1bb 55%,#f4dc72 100%)}

.title{position:absolute;top:232px;width:100%;text-align:center;font-family:"Noto Serif JP",serif;font-weight:900;font-size:44px;line-height:68px;letter-spacing:1px}
.subtitle{position:absolute;top:362px;width:100%;text-align:center;font-family:"Noto Serif JP",serif;font-weight:700;font-size:24px;color:var(--green-dark)}
.subtitle-en{position:absolute;top:394px;width:100%;text-align:center;font-family:"Noto Serif JP",serif;font-size:19px;font-weight:700;color:var(--green-dark)}

.date{position:absolute;top:432px;width:100%;text-align:center;font-weight:700;font-size:42px;letter-spacing:1px}
.date .small{font-size:30px}
.date .weekday{display:inline-block;width:36px;height:36px;border-radius:50%;background:var(--green);color:var(--white);font-size:22px;line-height:36px;vertical-align:6px;margin:0 8px 0 4px}
.venue{position:absolute;top:486px;width:100%;text-align:center;font-weight:700;font-size:26px;line-height:32px}
.venue .room{font-size:22px}

.person{position:absolute;left:160px;display:flex;align-items:flex-start;gap:36px}
.person.chair{top:576px}
.person.speaker{top:716px}
.role{width:70px;height:70px;border-radius:50%;background:var(--green);color:var(--white);font-weight:700;font-size:22px;display:flex;align-items:center;justify-content:center;writing-mode:vertical-rl;letter-spacing:4px;flex-shrink:0}
.person-name{font-weight:700;font-size:30px;line-height:44px;padding-top:2px;white-space:nowrap}
.person-name .hon{font-size:28px;margin-left:30px}
.person-name .gap{margin-left:22px}
.affil{font-size:15px;line-height:21px;font-weight:500}
.affil .indent{padding-left:150px}

.cohost{position:absolute;top:1104px;width:100%;text-align:center;font-size:17px;line-height:24px;font-weight:500}
</style>
</head>
<body>
<div class="flyer">
  <header class="header">
    <div class="society-mark"><span class="square"></span><span class="name">嚥下ケア看護会</span></div>
    <div class="sponsor-mark"><span class="dot"></span><span class="name">ハーモニア</span></div>
    <p class="congress">第 25 回日本嚥下ケア看護学会学術大会</p>
    <p class="seminar-no">ランチョンセミナー 15</p>
  </header>

  <div class="floral-field" role="img" aria-label="淡い黄色の地に白い桜の花びらが散る背景"></div>

  <h1 class="title">これからの摂食嚥下障害看護に<br>何が求められているか</h1>
  <p class="subtitle">～「機能低下予防」と「終末期 care」～</p>
  <p class="subtitle-en">What is required the future for dysphagia nursing</p>

  <p class="date">2019<span class="small"> 年 </span>9<span class="small"> 月 </span>7<span class="small"> 日</span><span class="weekday">土</span>12:00～13:00</p>
  <p class="venue"><span class="room">第 8 会場</span><br>港メッセ 海浜コンベンションセンター<br><span class="room">2F　中会議室　201</span></p>

  <section class="person chair">
    <div class="role">座長</div>
    <div>
      <p class="person-name">森川<span class="gap">陽子</span><span class="hon">先生</span></p>
      <p class="affil">瀬戸内看護大学　名誉教授</p>
    </div>
  </section>

  <section class="person speaker">
    <div class="role">演者</div>
    <div>
      <p class="person-name">高野<span class="gap">理恵</span><span class="hon">先生</span></p>
      <p class="affil">公益社団法人中部県看護協会<br><span class="indent">認定看護師教育課程主任</span><br>摂食・嚥下障害看護認定看護師教育課程　主任教員</p>
    </div>
  </section>

  <footer class="cohost">共催<br>第 25 回日本嚥下ケア看護学会学術大会<br>ハーモニア株式会社</footer>
</div>
</body>
</html>
```